Business Card Design

We develop / design / build affordable housing throughout the state of Illinois.

Target Market(s)

non profit organizations and other developers / professionals in my industry

Industry/Entity Type

Business

Contact Information for Business Card

Verdell Ridge Construction, LLC
General Contracting
Marisol K Thornbury, CEO
418 North Wendell P Ashcroft Avenue, Suite 307
Brenmoor, IL 60999
630-555-0148
mkt@buildverdellridge.com

```html
<!DOCTYPE html>
<html lang="en">
<head>
<meta charset="utf-8">
<title>Verdell Ridge Construction – Business Card</title>
<link href="https://fonts.googleapis.com/css2?family=Tinos:wght@400;700&display=swap" rel="stylesheet">
<style>
  :root {
    --backdrop: #ecebe8;
    --card: #2f2c2b;
    --ink-light: #f4f1ec;
    --ink-soft: #e2ddd6;
    --gold-dark: #a67c55;
    --gold-mid: #d9b994;
    --gold-light: #f6e3cb;
    --logo-paper: #ffffff;
    --logo-ink: #3a3a3a;
  }
  * { box-sizing: border-box; margin: 0; padding: 0; }
  html, body {
    width: 1200px; height: 773px; overflow: hidden;
    background: var(--backdrop);
    font-family: "Tinos", "Times New Roman", serif;
  }
  .sheet {
    width: 1200px; height: 773px;
    display: flex; flex-direction: column; align-items: center; justify-content: center;
    gap: 40px;
  }
  .card {
    position: relative;
    width: 560px; height: 320px;
    background: var(--card);
    color: var(--ink-light);
    box-shadow: 0 6px 18px rgba(0,0,0,0.18);
    overflow: hidden;
  }
  .card__edge-band {
    position: absolute; left: 0; top: 0; bottom: 0; width: 40px;
    background: linear-gradient(90deg, var(--gold-dark), var(--gold-light) 45%, var(--gold-mid) 75%, var(--gold-dark));
  }
  .card__rule {
    position: absolute; left: 40px; right: 0; top: 168px; height: 10px;
    background: linear-gradient(90deg, var(--gold-dark), var(--gold-light) 40%, var(--gold-mid) 70%, var(--gold-dark));
  }
  .logo-mark {
    position: absolute; left: 62px; top: 44px; width: 92px; height: 92px;
    background: var(--logo-paper);
    display: flex; flex-direction: column; align-items: center; justify-content: center; gap: 8px;
  }
  .logo-mark__square { width: 30px; height: 30px; background: var(--logo-ink); }
  .logo-mark__name {
    font-size: 9px; color: var(--logo-ink); text-align: center; line-height: 1.15; padding: 0 4px;
  }
  .identity {
    position: absolute; right: 56px; top: 36px; text-align: right;
  }
  .identity__company { font-weight: 700; font-size: 21px; }
  .identity__trade { font-weight: 700; font-size: 17px; margin-top: 6px; margin-right: 56px; }
  .identity__person { font-weight: 700; font-size: 24px; margin-top: 22px; }
  .contact {
    position: absolute; right: 16px; top: 196px; text-align: right;
    font-size: 15.5px; line-height: 1.3; color: var(--ink-soft); font-style: normal;
  }
  .contact__label { font-weight: 700; }
  .card--back { display: flex; flex-direction: column; align-items: center; justify-content: center; gap: 22px; }
  .back__company { font-weight: 700; font-size: 26px; }
  .back__trade { font-weight: 700; font-size: 21px; }
</style>
</head>
<body>
<main class="sheet">
  <section class="card card--front">
    <div class="card__edge-band" role="img" aria-label="Gold marbled decorative band"></div>
    <div class="card__rule"></div>
    <div class="logo-mark">
      <span class="logo-mark__square"></span>
      <span class="logo-mark__name">Verdell Ridge Construction</span>
    </div>
    <div class="identity">
      <h1 class="identity__company">Verdell Ridge Construction, LLC</h1>
      <p class="identity__trade">General Contracting</p>
      <p class="identity__person">Marisol K Thornbury</p>
    </div>
    <address class="contact">
      <p><span class="contact__label">Address:</span>418 North Wendell P Ashcroft Avenue,</p>
      <p>Suite 307 Brenmoor, IL 60999</p>
      <p><span class="contact__label">Phone:</span>555-555-0148</p>
      <p><span class="contact__label">E-mai:</span>mkt@buildverdellridge.com</p>
    </address>
  </section>
  <section class="card card--back">
    <p class="back__company">Verdell Ridge Construction, LLC</p>
    <p class="back__trade">General Contracting</p>
  </section>
</main>
</body>
</html>
```